Website Redesign for Existing BBQ Catering Company

Need to get my website (HickoryHound.com) redesigned. Looking for a cleaner look but still patriotic and rustic. Would like to add parallax scrolling on the menu page and include some pics from our photo gallery. Would like to display a picture of the brisket before scrolling into the meat section of our menu and the same for the other sections too.....picture of one of our sides, appetizers, desserts, etc.

Would also like to add three new pages called Corporate Events, Weddings, and Veteran Events possibly in a drop-down menu called Catering. You can use pics from our Facebook page. We've posted tons of pics from weddings that we've done. I've uploaded some corporate and wedding pics but you can pics the ones that look best. I can swap them out later if needed.

Would like to keep it Wordpress if possible so I can update it as needed.

Also need to add some links to our storefront on The Vow Loft. I have the HTML code and will upload the image here.

Also need to add social media links for our Facebook, Instagram and Twitter pages.

The contact form that I'm using now feeds the leads into another site called Ledgerly.com that I use to manage my clients.

Target Market(s)

Weddings, corporate events, veterans

Industry/Entity Type

Catering

Coding

Coded - Design and coding required

Number of Pages Required

5+ page

Colors
ec1f27
3176b5
ffffff

Requirements
Must have
• Really like the hero image design. Looks less like a template. Check out https://maurins.com and https://fennelgrovetaos.com
• Would like to keep somewhat of a rustic and patriotic look and feel like the site currently is. We mainly cater in barn weddings and we cater for a lot of veterans. Will be pushing more corporate catering next year and opening a restaurant.

```html
<!DOCTYPE html>
<html lang="en">
<head>
<meta charset="utf-8">
<title>Veteran Events – Hickory Hound BBQ</title>
<link rel="stylesheet" href="https://fonts.googleapis.com/css2?family=Roboto:wght@500&family=Roboto+Slab:wght@700&family=Open+Sans:wght@400&display=swap">
<style>
  :root {
    --red: #ec1f27;
    --blue: #3176b5;
    --navy: #1f4e96;
    --white: #ffffff;
    --wood-dark: #2b1a10;
    --wood-mid: #4a2e1c;
    --paper: #ececec;
    --ink: #3a3a3a;
  }
  * { margin: 0; padding: 0; box-sizing: border-box; }
  html, body { width: 1179px; height: 1200px; overflow: hidden; }
  body { position: relative; background: var(--wood-dark); font-family: "Open Sans", sans-serif; }

  .wood-band {
    position: absolute; left: 0; width: 1179px;
    background: linear-gradient(180deg, var(--wood-mid) 0%, var(--wood-dark) 45%, #3b2416 70%, var(--wood-dark) 100%);
  }
  .wood-band--top { top: 0; height: 112px; z-index: 2; }
  .wood-band--bottom { top: 960px; height: 240px; }

  .hero-photo {
    position: absolute; left: 0; top: 112px; width: 1179px; height: 470px;
    background: linear-gradient(100deg, #5b6670 0%, #2a2a33 25%, #2c2b35 55%, #7a1f34 75%, #d8cfb8 85%, #7a1f34 100%);
  }
  .hero-title {
    position: absolute; top: 254px; left: 0; width: 1179px; text-align: center;
    font-family: "Roboto Slab", serif; font-weight: 700; font-size: 48px;
    color: var(--white); letter-spacing: 1px; z-index: 3;
  }

  .brand {
    position: absolute; left: 120px; top: 12px; width: 178px; height: 178px;
    border-radius: 50%; background: var(--white); border: 8px solid #c9ccd1;
    display: flex; align-items: center; justify-content: center; text-align: center;
    z-index: 5;
  }
  .brand__name {
    font-family: "Roboto Slab", serif; font-weight: 700; font-size: 22px;
    line-height: 1.15; color: var(--red); width: 130px;
  }

  .social { position: absolute; top: 20px; left: 941px; display: flex; gap: 7px; z-index: 4; }
  .social__link {
    width: 32px; height: 32px; border-radius: 50%;
    border: 2px solid var(--white); display: block;
  }

  .nav { display: flex; gap: 18px; position: absolute; z-index: 4; }
  .nav a {
    font-family: "Roboto", sans-serif; font-weight: 500; font-size: 14.5px;
    color: var(--white); text-decoration: none; text-transform: uppercase; white-space: nowrap;
  }
  .nav a.is-active { color: var(--red); }
  .nav--main { top: 69px; left: 337px; }
  .nav--footer { top: 1111px; left: 0; width: 1179px; justify-content: center; }

  .content-shape { position: absolute; left: 0; top: 0; width: 1179px; height: 1200px; z-index: 1; }

  .content { position: absolute; left: 0; top: 0; width: 1179px; z-index: 3; }
  .content__heading {
    position: absolute; top: 532px; left: 0; width: 1179px; text-align: center; padding-left: 36px;
    font-family: "Roboto Slab", serif; font-weight: 700; font-size: 33px; color: var(--red);
  }
  .content__text { position: absolute; left: 140px; top: 630px; width: 482px; color: var(--ink); }
  .content__lead { font-size: 16.5px; line-height: 25px; margin-bottom: 16px; }
  .content__body { font-size: 12.6px; line-height: 24.3px; }
  .content__photo {
    position: absolute; left: 659px; top: 609px; width: 411px; height: 260px;
    background: linear-gradient(180deg, #27406f 0%, #8a1d2a 40%, #d9d6d2 55%, #b51f2c 75%, #e7e4e0 100%);
  }

  .listing-badge {
    position: absolute; left: 544px; top: 1001px; width: 94px; height: 94px;
    border-radius: 50%; background: #8ec6e8; border: 3px solid var(--white); z-index: 4;
  }

  .copyright {
    position: absolute; top: 1144px; left: 0; width: 1179px; text-align: center;
    font-size: 12.5px; color: #d8d2cc; z-index: 4;
  }
  .copyright a { color: #d8d2cc; text-decoration: underline; }
</style>
</head>
<body>
  <div class="wood-band wood-band--top"></div>
  <div class="hero-photo" role="img" aria-label="Chalkboard reading thank you veterans beside an American flag on weathered wood"></div>
  <div class="wood-band wood-band--bottom"></div>

  <svg class="content-shape" viewBox="0 0 1179 1200" aria-hidden="true">
    <path d="M0 555 Q589.5 411 1179 555 L1179 993 Q589.5 1115 0 993 Z" fill="var(--paper)"/>
    <path d="M219 509 Q596 437 973 509" fill="none" stroke="var(--navy)" stroke-width="3"/>
    <path d="M0 993 Q589.5 1115 1179 993" fill="none" stroke="var(--red)" stroke-width="3"/>
  </svg>

  <header>
    <div class="brand"><span class="brand__name">Hickory Hound BBQ</span></div>
    <div class="social">
      <a class="social__link" href="#" aria-label="Social profile one"></a>
      <a class="social__link" href="#" aria-label="Social profile two"></a>
      <a class="social__link" href="#" aria-label="Social profile three"></a>
    </div>
    <nav class="nav nav--main">
      <a href="#">Home</a><a href="#">Menu</a><a href="#">Photo Gallery</a>
      <a href="#">Corporate Catering</a><a href="#">Weddings</a>
      <a href="#" class="is-active">Veteran Events</a><a href="#">Contact</a>
    </nav>
  </header>

  <h1 class="hero-title">VETERAN EVENTS</h1>

  <main class="content">
    <h2 class="content__heading">VETERAN EVENTS</h2>
    <div class="content__text">
      <p class="content__lead">Fusce ultricies orci ac feugiat suscipit leo massa sodales velit et scelerisque mi tortor at ipsum cligula augue</p>
      <p class="content__body">vestibulum ut commodo a mi Morbi ornare gravida elit Integer congue augue et malesuada iaculis ipsum dui aliquet felis at cursus magna nisl nec elit Praesent elementum elit at tellus nec ultricies sit amet porttitor mattis enim In massa libero interdum nec interdum vel blandit sed nulla In ullamcorper est eget tempor cursus neque mi consectetuer mi a ultricies massa est sed nisl Class aptent taciti sociosqu ad litora torquent per conubia</p>
    </div>
    <div class="content__photo" role="img" aria-label="Thank you veterans lettering over a distressed American flag"></div>
  </main>

  <footer>
    <a class="listing-badge" href="#" aria-label="The Vow Loft storefront"></a>
    <nav class="nav nav--footer">
      <a href="#">Home</a><a href="#">Menu</a><a href="#">Photo Gallery</a>
      <a href="#">Corporate Catering</a><a href="#">Weddings</a>
      <a href="#">Veteran Events</a><a href="#">Contact</a>
    </nav>
    <p class="copyright">© 2017 Company Name &nbsp;All right reserved. <a href="#">Term of Use</a></p>
  </footer>
</body>
</html>
```